Facebook Ad design

We need designed a Facebook ad for our solar system's. We want to advertise a 13.32kW system for $4499.

Including: Velmor Falcon QX 370W Panels and Pelmara inverters.

```html
<!DOCTYPE html>
<html lang="en">
<head>
<meta charset="utf-8">
<title>Solar System Offer – Facebook Ad</title>
<link rel="stylesheet" href="https://fonts.googleapis.com/css2?family=Oswald:wght@200;700&family=Montserrat:wght@300;700&display=swap">
<style>
  :root {
    --navy: #2d3247;
    --red: #c01f2f;
    --white: #ffffff;
  }
  * { margin: 0; padding: 0; box-sizing: border-box; }
  html, body { width: 1200px; height: 1200px; overflow: hidden; background: var(--white); }
  .ad { position: relative; width: 1200px; height: 1200px; overflow: hidden; background: var(--white); }
  .ad-art { position: absolute; inset: 0; }
  .headline { position: absolute; left: 72px; top: 50px; color: var(--navy); font-family: "Oswald", sans-serif; line-height: 1; }
  .headline-size { display: block; font-weight: 700; font-size: 146px; line-height: 146px; letter-spacing: -3px; }
  .headline-lead { display: block; font-weight: 200; font-size: 144px; line-height: 136px; letter-spacing: -2px; }
  .headline-price { display: block; font-weight: 700; font-size: 146px; line-height: 142px; color: var(--red); letter-spacing: -3px; }
  .specs { position: absolute; left: 73px; top: 936px; font-family: "Montserrat", sans-serif; color: var(--navy); }
  .specs-brand { font-weight: 700; font-size: 46px; line-height: 60px; }
  .specs-model { font-weight: 700; font-size: 46px; line-height: 58px; color: var(--red); }
  .specs-detail { font-weight: 300; font-size: 34px; line-height: 43px; letter-spacing: 0.5px; }
  .brand { position: absolute; left: 634px; top: 962px; width: 520px; font-family: "Montserrat", sans-serif; color: var(--navy); }
  .brand-name { margin-left: 144px; font-weight: 700; font-size: 58px; line-height: 62px; color: var(--navy); }
  .brand-tagline { margin-top: 24px; font-weight: 300; font-size: 21.5px; letter-spacing: 0.3px; white-space: nowrap; }
</style>
</head>
<body>
<main class="ad">
  <svg class="ad-art" width="1200" height="1200" viewBox="0 0 1200 1200">
    <defs>
      <linearGradient id="scene-tones" x1="0" y1="0" x2="0" y2="1">
        <stop offset="0" stop-color="#d6e3f1"/>
        <stop offset="0.4" stop-color="#eef3f9"/>
        <stop offset="0.62" stop-color="#f1f4f8"/>
        <stop offset="0.66" stop-color="#5a5fae"/>
        <stop offset="0.73" stop-color="#4b4f9e"/>
        <stop offset="0.76" stop-color="#8f879f"/>
        <stop offset="0.84" stop-color="#7f7690"/>
        <stop offset="0.87" stop-color="#e9dcc0"/>
        <stop offset="1" stop-color="#d9c7a4"/>
      </linearGradient>
    </defs>
    <rect class="scene-photo" x="0" y="0" width="1200" height="910" fill="url(#scene-tones)" role="img" aria-label="Photo of a modern flat-roofed house with rows of solar panels on the roof under a bright cloudy sky"/>
    <path class="swoosh-white" d="M0,800 Q560,975 1200,790 L1200,1200 L0,1200 Z" fill="var(--white)"/>
    <path class="swoosh-red" d="M0,762 Q530,955 1200,772 L1200,790 Q560,975 0,826 Z" fill="var(--red)"/>
    <path class="swoosh-navy" d="M630,903 Q960,882 1200,782 L1200,806 Q970,900 630,903 Z" fill="var(--navy)"/>
  </svg>

  <h1 class="headline">
    <span class="headline-size">13.32KW</span>
    <span class="headline-lead">SYSTEM FOR</span>
    <span class="headline-price">$4499</span>
  </h1>

  <section class="specs">
    <p class="specs-brand">VELMOR FALCON</p>
    <p class="specs-model">QX 370W</p>
    <p class="specs-detail">PANELS AND<br>PELMARA INVERTERS.</p>
  </section>

  <section class="brand">
    <p class="brand-name">CORVEL<br>ENERGY</p>
    <p class="brand-tagline">ENGINEERING AND ECONOMIC SOLUTIONS</p>
  </section>
</main>
</body>
</html>
```